Software Company Business Card

We are looking for a new design of our business card. The design will also be used in the rest of our branding and marketing materials as we want to keep it all uniform. We sell POS software to fine/luxury jewelers and also offer other business services as well to help the jeweler manage their business and need something more updated, technical and fresh, preferably more on the masculine side. We do not want any designs with gems in them but if possible would like to incorporate the circle and arrow in the logo into the design, but not a requirement if you can't make it work. I would like to see a variety of the mix. The colors need to remain our blue and orange and the logo can not change. The squiggly lines have been used as our corporate identity for over 20 years and its time to update. Our company name is PELK (Bright Ledger Counter Solutions).

Target Market(s)

High End Jewelers

Industry/Entity Type

Software

Contact Information for Business Card

Requirements
Must have
• Our logo and the colors must remain the same. Blue is #d95d39 and Orange is #0f5682.
Nice to have
• The circle and arrow incorporated but not a requirement.
Should not have
• Anything jewelry or gem related.

```html
<!DOCTYPE html>
<html lang="en">
<head>
<meta charset="utf-8">
<title>PELK Business Card</title>
<link href="https://fonts.googleapis.com/css2?family=Archivo:wght@400;500;700;900&display=swap" rel="stylesheet">
<style>
  :root {
    --orange: #d95d39;
    --blue: #0f5682;
    --paper: #f4f4f3;
    --ink-blue: #0f5682;
    --stage: #141414;
    --gold: #c9a35a;
    --sage: #8fb3a2;
    --white: #ffffff;
  }
  * { margin: 0; padding: 0; box-sizing: border-box; }
  html, body {
    width: 1200px; height: 820px; overflow: hidden;
    background: var(--stage);
    font-family: "Archivo", Arial, sans-serif;
  }
  .canvas {
    width: 1200px; height: 820px;
    display: flex; align-items: center; justify-content: center; gap: 50px;
  }
  .card {
    position: relative;
    width: 525px; height: 300px;
    border-radius: 4px;
    overflow: hidden;
    box-shadow: 0 18px 40px rgba(0,0,0,.55);
  }

  /* Name plate: plain square, then the company name in one weight */
  .name-plate {
    position: absolute; display: flex; align-items: center; gap: 12px;
    font-weight: 700; letter-spacing: 3px; line-height: 1;
  }
  .name-plate-square { flex: none; }

  /* Front */
  .card-front { background: var(--paper); }
  .card-front .name-plate { left: 38px; top: 40px; font-size: 44px; color: var(--blue); }
  .card-front .name-plate-square { width: 16px; height: 16px; background: var(--orange); }

  .person { position: absolute; left: 38px; top: 120px; }
  .person-name { font-weight: 700; font-size: 23px; color: var(--ink-blue); letter-spacing: -.3px; }
  .person-title { font-weight: 700; font-size: 11px; color: var(--orange); letter-spacing: .6px; margin-top: 3px; }

  .contact-list { position: absolute; left: 38px; top: 178px; list-style: none; }
  .contact-list li {
    display: flex; align-items: center; gap: 9px;
    font-size: 11.5px; color: var(--ink-blue); line-height: 1.25; margin-bottom: 5px;
  }
  .icon-badge {
    width: 19px; height: 19px; border-radius: 50%; background: var(--orange);
    display: flex; align-items: center; justify-content: center; flex: none;
  }
  .icon-badge svg { width: 11px; height: 11px; }

  .partner-badges { position: absolute; right: 48px; top: 88px; display: flex; gap: 30px; align-items: center; }
  .partner-badge { width: 44px; height: 44px; border-radius: 50%; }
  .partner-badge.gold { background: var(--gold); opacity: .8; }
  .partner-badge.sage { background: var(--sage); opacity: .7; }

  .phone-list { position: absolute; right: 34px; top: 176px; list-style: none; }
  .phone-list li {
    display: flex; align-items: center; gap: 8px;
    font-size: 12px; color: var(--ink-blue); margin-bottom: 6px;
  }

  .brand-band {
    position: absolute; left: 0; right: 0; bottom: 0; height: 30px;
    background: linear-gradient(90deg, var(--orange) 0%, #a45a58 45%, var(--blue) 100%);
    display: flex; align-items: center; justify-content: flex-end; padding-right: 26px;
  }
  .tagline { color: var(--white); font-size: 10px; letter-spacing: .8px; font-weight: 500; }

  /* Back */
  .card-back {
    background: linear-gradient(115deg, var(--orange) 0%, var(--orange) 30%, #8e5b61 52%, var(--blue) 80%, var(--blue) 100%);
  }
  .back-lockup {
    position: absolute; inset: 0;
    display: flex; flex-direction: column; align-items: center; justify-content: center; gap: 10px;
  }
  .card-back .name-plate { position: static; font-size: 44px; color: var(--white); }
  .card-back .name-plate-square { width: 16px; height: 16px; background: var(--white); }
  .back-tagline {
    color: var(--white); font-weight: 700; font-size: 9.5px; letter-spacing: .8px;
  }
</style>
</head>
<body>
<main class="canvas">

  <section class="card card-front" aria-label="Business card front">
    <div class="name-plate"><span class="name-plate-square"></span><span>PELK</span></div>

    <div class="person">
      <p class="person-name">Dorian Vance</p>
      <p class="person-title">DIRECTOR OF GLOBAL OPERATIONS</p>
    </div>

    <ul class="contact-list">
      <li>
        <span class="icon-badge"><svg viewBox="0 0 12 12"><rect x="1" y="2.5" width="10" height="7" fill="none" stroke="#fff" stroke-width="1.2"/><path d="M1 3l5 4 5-4" fill="none" stroke="#fff" stroke-width="1.2"/></svg></span>
        <span>dorian@pelkhq.com</span>
      </li>
      <li>
        <span class="icon-badge"><svg viewBox="0 0 12 12"><circle cx="6" cy="6" r="4.6" fill="none" stroke="#fff" stroke-width="1.1"/><ellipse cx="6" cy="6" rx="2" ry="4.6" fill="none" stroke="#fff" stroke-width="1"/><path d="M1.4 6h9.2" stroke="#fff" stroke-width="1"/></svg></span>
        <span>www.pelkhq.com</span>
      </li>
      <li>
        <span class="icon-badge"><svg viewBox="0 0 12 12"><path d="M6 11S2.2 6.8 2.2 4.5a3.8 3.8 0 0 1 7.6 0C9.8 6.8 6 11 6 11z" fill="#fff"/><circle cx="6" cy="4.5" r="1.3" fill="#d95d39"/></svg></span>
        <span>418 Meridian Loop Suite 210<br>Carrow Falls, NV 89011 USA</span>
      </li>
    </ul>

    <div class="partner-badges">
      <span class="partner-badge gold" role="img" aria-label="Partner show badge"></span>
      <span class="partner-badge sage" role="img" aria-label="Trade association badge"></span>
    </div>

    <ul class="phone-list">
      <li>
        <span class="icon-badge"><svg viewBox="0 0 12 12"><path d="M3 1.5l1.6 2.2-1 1.1a6 6 0 0 0 3.6 3.6l1.1-1 2.2 1.6-.8 1.6C5.6 10.4 1.6 6.4 1.4 2.3z" fill="#fff"/></svg></span>
        <span>+1 800 555-0142</span>
      </li>
      <li>
        <span class="icon-badge"><svg viewBox="0 0 12 12"><rect x="3" y="1.5" width="6" height="3" fill="#fff"/><rect x="1.5" y="4.5" width="9" height="4" rx=".8" fill="#fff"/><rect x="3" y="7.5" width="6" height="3" fill="#fff" stroke="#d95d39" stroke-width=".6"/></svg></span>
        <span>702 555-0187</span>
      </li>
    </ul>

    <div class="brand-band"><span class="tagline">BUSINESS &amp; TECHNOLOGY SOLUTIONS</span></div>
  </section>

  <section class="card card-back" aria-label="Business card back">
    <div class="back-lockup">
      <div class="name-plate"><span class="name-plate-square"></span><span>PELK</span></div>
      <p class="back-tagline">BUSINESS &amp; TECHNOLOGY SOLUTIONS</p>
    </div>
  </section>

</main>
</body>
</html>
```